UL Aesthetic improvement on full website

marbleferngo.com
We need someone to improve the current website marbleferngo.com
Some designed to fail to follow isntruction and deliver. please find attached summary latest design requirement, please follow and read each of the requirements carefully and submit max two versions only. The winner would have to deliver within 5 days

Sample reference : pelorix.com/html/marblefern/#
(previous winner cant deliver)
*All of our wording and graphic content are updated, designer wouldn't involve in recreating any content.
Designer may use template or own material. delivery in html and implement on our WordPress server

please submit about us the project submission.
upon the winning, you have to maintain sub content / pages and submit the full site with your improved version of full websites including inner pages

Low design quality

Target Market(s)

general audience

Industry/Entity Type

social service

Number of Pages Required

5+ page

Requirements
Must have
• feeling and look similar to quenvo dot com
Nice to have
• extend the same style to other pages

```html
<!DOCTYPE html>
<html lang="en">
<head>
<meta charset="utf-8">
<title>Marble Fern – New way of Giving</title>
<link href="https://fonts.googleapis.com/css2?family=Poppins:wght@300;400;500;600;700&display=swap" rel="stylesheet">
<style>
:root{
  --pink:#ef5a6a;
  --pink-soft:#fde9ea;
  --ink:#1c1c1f;
  --muted:#7b7b86;
  --band:#f1f0f5;
  --line:#ececf0;
  --white:#ffffff;
}
*{box-sizing:border-box;margin:0;padding:0}
html,body{width:1200px;height:4152px;overflow:hidden}
body{position:relative;background:var(--white);font-family:'Poppins',sans-serif;color:var(--ink)}
.abs{position:absolute}
.eyebrow{font-size:11px;font-weight:600;letter-spacing:1.5px;color:var(--pink);text-transform:uppercase}
.accent{color:var(--pink)}
.body-text{font-size:13px;line-height:22px;color:var(--muted)}
.btn-dark{display:inline-block;background:var(--ink);color:var(--white);font-size:13px;font-weight:500;border-radius:22px;padding:11px 28px}

/* header */
.site-header{top:0;left:0;width:1200px;height:86px}
.brand{left:40px;top:18px;display:flex;align-items:center;gap:12px;font-size:16px;font-weight:600;color:var(--ink)}
.brand-dot{width:48px;height:48px;border-radius:50%;background:var(--pink)}
.main-nav{left:560px;top:33px;display:flex;gap:34px;font-size:13px;font-weight:500}
.nav-signup{left:1030px;top:22px;padding:10px 28px}

/* hero */
.hero-text{left:60px;top:292px;width:420px}
.hero-title{font-size:40px;line-height:50px;font-weight:600;margin:10px 0 14px}
.hero-art{left:540px;top:96px;width:620px;height:540px;border-radius:46% 54% 44% 56%/52% 46% 54% 48%;background:radial-gradient(circle at 55% 50%,#f8747f 0 48%,#fcd6da 49% 62%,#fff 63%)}

/* about */
.about-media{left:60px;top:740px;width:440px;height:240px;border-radius:6px;background:linear-gradient(135deg,#cfe3e6,#f3c9c9 60%,#e4d9ee)}
.play{left:260px;top:840px;width:44px;height:44px;border-radius:50%;background:var(--ink);display:flex;align-items:center;justify-content:center}
.about-text{left:640px;top:748px;width:520px}
.section-title{font-size:30px;font-weight:600;line-height:40px;margin:8px 0 12px}
.band{left:0;width:1200px}

/* audience cards */
.audience-card{top:1290px;height:290px;background:var(--white);border-radius:6px;box-shadow:0 6px 24px rgba(30,30,40,.08);text-align:center;padding:26px 26px}
.card-art{width:120px;height:96px;margin:0 auto 18px;border-radius:10px;background:linear-gradient(135deg,#fbd0d5,#f6929c)}
.card-title{font-size:15px;font-weight:600;margin-bottom:10px}
.card-text{font-size:12px;line-height:20px;color:var(--muted)}

/* story */
.story-art{left:60px;top:1670px;width:500px;height:360px;border-radius:6px;background:linear-gradient(135deg,#f3ede4,#e96e64 45%,#2e3f8f 80%,#f3d45a)}
.story-text{left:640px;top:1680px;width:520px}

/* glance */
.centered{left:0;width:1200px;text-align:center}
.glance-card{top:2260px;width:304px;height:204px;border-radius:8px;overflow:hidden;color:var(--white)}
.glance-card .shade{position:absolute;left:0;right:0;bottom:0;padding:16px 18px;background:linear-gradient(to top,rgba(20,20,25,.75),rgba(20,20,25,0))}
.glance-title{font-size:16px;font-weight:600}
.glance-text{font-size:11px;line-height:16px;opacity:.9}

/* ambassadors */
.person{top:2840px;width:250px;height:360px;background:var(--white);box-shadow:0 6px 24px rgba(30,30,40,.08);border-radius:4px;overflow:hidden}
.person-photo{height:250px;background:linear-gradient(160deg,#d9d2cb,#8d8479)}
.person-info{padding:14px 18px;font-size:13px;line-height:21px;color:var(--muted)}
.person-info strong{color:var(--ink);font-weight:600}

/* contact */
.contact-text{left:60px;top:3310px;width:500px}
.contact-photo{left:628px;top:3310px;width:512px;height:350px;border-radius:4px;background:linear-gradient(180deg,#e9eef2 0 35%,#5c8b6c 36% 52%,#8fb5c6 53%)}

/* footer */
.site-footer{left:0;top:3740px;width:1200px;height:412px;background:var(--pink-soft)}
.footer-brand{left:60px;top:3830px;width:240px}
.footer-brand .brand-dot{width:56px;height:56px;margin-bottom:14px}
.footer-head{font-size:14px;font-weight:600;margin-bottom:10px}
.footer-small{font-size:11px;line-height:18px;color:var(--muted)}
.socials{display:flex;gap:10px;margin-top:16px}
.socials span{width:26px;height:26px;border-radius:50%;background:var(--pink)}
.links{top:3830px}
.links ul{list-style:none;font-size:12px;line-height:30px;color:var(--muted)}
.newsletter{left:890px;top:3830px;width:250px}
.field{height:38px;border-radius:20px;background:var(--white);font-size:11px;color:var(--muted);padding:11px 16px;margin:12px 0}
.check{display:flex;gap:8px;align-items:flex-start}
.check i{flex:none;width:12px;height:12px;border:1px solid var(--muted);border-radius:2px;margin-top:3px}
.btn-pink{display:block;text-align:center;background:var(--pink);color:var(--white);font-size:12px;font-weight:500;border-radius:20px;padding:10px 0;margin-top:14px}
.copyright{left:0;top:4110px;width:1200px;text-align:center;font-size:11px;color:var(--muted)}
</style>
</head>
<body>

<header class="abs site-header">
  <div class="abs brand"><span class="brand-dot"></span>Marble Fern</div>
  <nav class="abs main-nav"><span>Home</span><span>About</span><span>Our Story</span><span>Social Impact</span><span>Join Us</span></nav>
  <span class="abs btn-dark nav-signup">Sign Up</span>
</header>

<section>
  <div class="abs hero-art" role="img" aria-label="App screens on phones over a pink blob"></div>
  <div class="abs hero-text">
    <p class="eyebrow">Welcome</p>
    <h1 class="hero-title">New way of Giving<br><span class="accent">Social Inclusion</span></h1>
    <p class="body-text">We believe in authentic social responsibility is driven<br>from individuals and businesses.</p>
  </div>
</section>

<svg class="abs band" style="top:900px" width="1200" height="300" viewBox="0 0 1200 300" aria-hidden="true">
  <path d="M0 70 C300 10 700 130 1200 40 L1200 220 C850 300 400 170 0 250 Z" fill="var(--band)"/>
</svg>

<section>
  <div class="abs about-media" role="img" aria-label="Video still of a colourful illustrated city scene"></div>
  <div class="abs play"><svg width="14" height="16" viewBox="0 0 14 16"><path d="M2 1 L13 8 L2 15 Z" fill="#fff"/></svg></div>
  <div class="abs about-text">
    <p class="eyebrow">About us</p>
    <h2 class="section-title">Hello, <span class="accent">Marble</span> Ferns!</h2>
    <p class="body-text">Just like you, we resonate with a variety of social causes. At the core of everything, we believe that many societal challenges could be minimised simply by being more kind to one another and showing more trust in each other, especially during these difficult times.</p>
  </div>
</section>

<section>
  <div class="abs audience-card" style="left:60px;width:300px">
    <div class="card-art" role="img" aria-label="Illustration of friendly citizens"></div>
    <h3 class="card-title">Fern Citizens</h3>
    <p class="card-text">You might be a busy professional with a strong desire to help our community positively and kindly.</p>
  </div>
  <div class="abs audience-card" style="left:450px;width:300px">
    <div class="card-art" role="img" aria-label="Illustration of a business team"></div>
    <h3 class="card-title">Fern Business</h3>
    <p class="card-text">Traditionally, corporate social responsibility has been the big-push effort, which we now make simpler.</p>
  </div>
  <div class="abs audience-card" style="left:800px;width:340px">
    <div class="card-art" role="img" aria-label="Illustration of a shop front"></div>
    <h3 class="card-title">Merchant</h3>
    <p class="card-text">At Marble Fern, we make it convenient and easy to blend social impact in your shop every day.</p>
  </div>
</section>

<section>
  <div class="abs story-art" role="img" aria-label="Colourful abstract illustration of hands and shapes"></div>
  <div class="abs story-text">
    <p class="eyebrow">It starts from you</p>
    <h2 class="section-title">The <span class="accent">Brand</span> Story</h2>
    <p class="body-text">Back in the 1980s, my family received generous donations and small handwritten notes containing good wishes through a newspaper fund, making life easier for my mum's medical expenses and reminding us that kindness travels far.</p>
  </div>
</section>

<section>
  <div class="abs centered" style="top:2120px">
    <p class="eyebrow">Social inclusion</p>
    <h2 class="section-title"><span class="accent">Fern</span> Citizens At A Glance</h2>
    <p class="body-text">We believe in authentic social responsibility is driven from individuals<br>and businesses.</p>
  </div>
  <div class="abs glance-card" style="left:128px;background:linear-gradient(135deg,#6f8f7a,#2f3d36)" role="img" aria-label="Photo of volunteers sorting waste">
    <div class="shade"><p class="glance-title">Waste Minimization</p><p class="glance-text">Reducing waste together through everyday small choices.</p></div>
  </div>
  <div class="abs glance-card" style="left:448px;background:linear-gradient(135deg,#b9867a,#3d2b2a)" role="img" aria-label="Photo of hands joined together">
    <div class="shade"><p class="glance-title">Social Impact</p><p class="glance-text">There is a better way to make donations count today.</p></div>
  </div>
  <div class="abs glance-card" style="left:768px;background:linear-gradient(135deg,#e7d9cf,#8a6b5c)" role="img" aria-label="Photo of ambassadors holding signs">
    <div class="shade"><p class="glance-title">Fern Ambassador</p><p class="glance-text">There is a better way to make donations count today.</p></div>
  </div>
</section>

<svg class="abs band" style="top:2470px" width="1200" height="190" viewBox="0 0 1200 190" aria-hidden="true">
  <path d="M0 40 C350 0 800 90 1200 20 L1200 130 C800 190 350 110 0 170 Z" fill="var(--band)"/>
</svg>

<section>
  <div class="abs centered" style="top:2715px">
    <p class="eyebrow">Social impact</p>
    <h2 class="section-title">Our <span class="accent">Social</span> Impact <span class="accent">Ambassadors</span> and Mentors</h2>
    <p class="body-text" style="font-size:12px">Social inclusion ensures no one is left out</p>
  </div>
  <div class="abs person" style="left:60px"><div class="person-photo" role="img" aria-label="Portrait photo of an ambassador" style="background:linear-gradient(160deg,#3a3a3e,#1e1e22)"></div><div class="person-info"><strong>Name</strong><br>Company<br>Designation</div></div>
  <div class="abs person" style="left:330px"><div class="person-photo" role="img" aria-label="Portrait photo of an ambassador" style="background:linear-gradient(160deg,#e6d6c8,#a7725a)"></div><div class="person-info"><strong>Name</strong><br>Company<br>Designation</div></div>
  <div class="abs person" style="left:600px"><div class="person-photo" role="img" aria-label="Portrait photo of a mentor" style="background:linear-gradient(160deg,#cfcfd3,#3c3f4a)"></div><div class="person-info"><strong>Name</strong><br>Company<br>Designation</div></div>
  <div class="abs person" style="left:890px"><div class="person-photo" role="img" aria-label="Photo of a mentor sitting outdoors" style="background:linear-gradient(160deg,#f1d7c2,#b9825e)"></div><div class="person-info"><strong>Name</strong><br>Company<br>Designation</div></div>
</section>

<section>
  <div class="abs contact-text">
    <p class="eyebrow">Contact us</p>
    <h2 class="section-title">Get In <span class="accent">Touch</span> With Us</h2>
    <p class="body-text">We connect individuals and businesses to support where it needs most in an easy, transparent, and fulfilled way through our platform.</p>
    <p class="body-text" style="margin:14px 0 22px">Together, social impact is part of lives at the heart of every consumption and business.</p>
    <span class="btn-dark">Contact Us</span>
  </div>
  <div class="abs contact-photo" role="img" aria-label="Photo of a calm lake lined with trees"></div>
</section>

<footer>
  <div class="abs site-footer"></div>
  <svg class="abs band" style="top:3700px" width="1200" height="80" viewBox="0 0 1200 80" aria-hidden="true">
    <path d="M0 40 C300 80 800 0 1200 40 L1200 80 L0 80 Z" fill="var(--pink-soft)"/>
  </svg>
  <div class="abs footer-brand">
    <div class="brand-dot"></div>
    <p class="footer-head" style="margin-bottom:6px">Follow us and stay updated!</p>
    <p class="footer-small">A social enterprise in a world where you can do anything, be kind.</p>
    <div class="socials"><span></span><span></span><span></span></div>
  </div>
  <div class="abs links" style="left:340px">
    <p class="footer-head">Useful Links</p>
    <ul><li>Home</li><li>About Us</li><li>Our Story</li><li>Social Impact</li><li>Fern Citizen</li></ul>
  </div>
  <div class="abs links" style="left:620px;top:3860px">
    <ul><li>Fern Business</li><li>Merchant</li><li>The Fern 100</li><li>FAQs</li><li>Contact Us</li></ul>
  </div>
  <div class="abs newsletter">
    <p class="footer-head">Subscribe to Our Newsletter</p>
    <p class="footer-small">Let's stay in touch. We would like to keep you inspired with our kindness stories and community events.</p>
    <div class="field">Enter email here</div>
    <div class="check footer-small"><i></i><span>By continuing, you accept the privacy policy.</span></div>
    <span class="btn-pink">Subscribe Now</span>
  </div>
  <p class="abs copyright">© Marble Fern – 2021 – All Rights Reserved</p>
</footer>

</body>
</html>
```